Large multi-office optometry business opening a Dry Eye Spa and needs sign.

Business name/sign info: Brindlecove Dry Eye Institute, (555) 316-4872
Backlit pole sign at office entrance on a very busy street
Sign dimensions: 53" tall x 136.5" wide
State of the art Dry Eye Spa for treatment of all forms of dry eye and ocular surface disease. Also, have aesthetics treatments (IPL, Low Level Light Treatment, etc.)

Target Market(s)

People who are suffering from: dryness, burning, foreign body sensation, itching, fluctuating vision, tired eyes, etc.

Industry/Entity Type

Optometry and aesthetics

Colors
0054AA
0677BA
7BADD7
CADEEF
E8F1F8

Requirements
Must have
• Business name, phone number, subliminal message of relief in a glance or short look.
Nice to have
• Cool, relief, soothing sense.
Should not have
• Too much information or too busy.

```html
<!DOCTYPE html>
<html lang="en">
<head>
<meta charset="utf-8">
<title>Brindlecove Dry Eye Institute – Pole Sign</title>
<link href="https://fonts.googleapis.com/css2?family=Poppins:wght@700;800&family=Montserrat:wght@800&display=swap" rel="stylesheet">
<style>
  :root {
    --navy: #05087f;
    --signal-red: #ff0000;
    --white: #ffffff;
    --sky-pale: #e8f1f8;
    --sky-soft: #cadeef;
    --sky-mid: #7badd7;
    --aqua: #2cc3de;
    --ocean: #0677ba;
  }
  html, body {
    margin: 0;
    padding: 0;
    overflow: hidden;
    background: var(--white);
  }
  .sign {
    position: relative;
    width: 1200px;
    height: 466px;
    overflow: hidden;
    font-family: "Poppins", sans-serif;
  }
  .sign__backdrop {
    position: absolute;
    inset: 0;
    width: 100%;
    height: 100%;
  }
  .sign__splash {
    position: absolute;
    left: 20px;
    top: 56px;
    width: 330px;
    height: 372px;
    border-radius: 50% 50% 40% 60% / 40% 40% 60% 60%;
    background: radial-gradient(ellipse at 55% 45%, rgba(255,255,255,0.25) 0%, #6fcdee 35%, #2aa6da 75%, rgba(42,166,218,0.4) 100%);
    opacity: 0.85;
  }
  .sign__name {
    position: absolute;
    left: 375px;
    top: 152px;
    width: 770px;
    margin: 0;
    text-align: center;
    font-family: "Poppins", sans-serif;
    font-weight: 700;
    font-size: 64px;
    line-height: 76px;
    letter-spacing: 1px;
    color: var(--navy);
    white-space: nowrap;
  }
  .sign__name span { display: block; }
  .sign__tagline {
    position: absolute;
    left: 375px;
    top: 320px;
    width: 770px;
    height: 45px;
    margin: 0;
    background: var(--signal-red);
    color: var(--white);
    font-family: "Montserrat", sans-serif;
    font-weight: 800;
    font-size: 34px;
    letter-spacing: 3px;
    line-height: 45px;
    text-align: center;
    white-space: nowrap;
  }
  .sign__phone {
    position: absolute;
    left: 375px;
    top: 396px;
    width: 770px;
    margin: 0;
    text-align: center;
    font-family: "Poppins", sans-serif;
    font-weight: 800;
    font-size: 56px;
    line-height: 66px;
    letter-spacing: 1px;
    color: var(--navy);
  }
</style>
</head>
<body>
<main class="sign">
  <svg class="sign__backdrop" viewBox="0 0 1200 466" preserveAspectRatio="none" aria-hidden="true">
    <defs>
      <linearGradient id="oceanFill" x1="0" y1="0" x2="1" y2="1">
        <stop offset="0" stop-color="#58cde6"/>
        <stop offset="0.6" stop-color="#2cc3de"/>
        <stop offset="1" stop-color="#1e9fd0"/>
      </linearGradient>
      <linearGradient id="skyFill" x1="0" y1="0" x2="1" y2="0.3">
        <stop offset="0" stop-color="#e4f4fa"/>
        <stop offset="0.35" stop-color="#f1f6fd"/>
        <stop offset="0.75" stop-color="#cdeaf5"/>
        <stop offset="1" stop-color="#2bb6e0"/>
      </linearGradient>
      <linearGradient id="bandFill" x1="0" y1="0" x2="1" y2="0">
        <stop offset="0" stop-color="#ffffff" stop-opacity="0.9"/>
        <stop offset="0.6" stop-color="#bfe7f2" stop-opacity="0.7"/>
        <stop offset="1" stop-color="#7fd3ea" stop-opacity="0.3"/>
      </linearGradient>
    </defs>
    <rect class="ocean" width="1200" height="466" fill="url(#oceanFill)"/>
    <path class="sky-band" d="M0 0 H1200 V170 C1050 250 820 340 560 380 C420 400 300 400 230 370 C120 330 40 270 0 170 Z" fill="url(#bandFill)"/>
    <path class="sky" d="M0 0 H1200 V120 C1120 190 900 270 700 300 C520 330 360 390 240 370 C120 340 20 260 0 170 Z" fill="url(#skyFill)"/>
  </svg>

  <div class="sign__splash" role="img" aria-label="Illustration of a curling splash of clear blue water with droplets"></div>

  <h1 class="sign__name"><span>BRINDLECOVE</span><span>DRY EYE INSTITUTE</span></h1>

  <p class="sign__tagline">FEEL THE RELIEF WITH A BLINK</p>

  <p class="sign__phone">(555) 316-4872</p>
</main>
</body>
</html>
```